Billboard design - consider what a billboard is

Design a billboard using my logo - Billboard is 6m x 3m
A Billboard is advertising for my company that is on a big sign.

Has to be clean and easy to read, and ideally highlights that we are Residential and Commercial builders.

Keep it clean and easy to read

The contact number for the board is

022 583 7092
www.harbourframeworks.co.nz
info@harbourframeworks.co.nz

Doesnt have to have all contact details if it doesnt fit

Has to catch peoples attention to contact us if they need a builder

Can you please change the sign to be all white writing, with black background ?
Updates

Please consider what a billboard is...

The design needs to be suitable for a billboard..

Target Market(s)

people driving past

Industry/Entity Type

Construction

Logo Text

Wellington Builder, website email address, contact number

Colors
0054AA
0677BA
7BADD7
CADEEF
E8F1F8

Requirements
Must have
• Easy to read
Nice to have
• easy to read, can clearly see contact details

```html
<!DOCTYPE html>
<html lang="en">
<head>
<meta charset="utf-8">
<title>Harbour Frameworks Billboard</title>
<link rel="stylesheet" href="https://fonts.googleapis.com/css2?family=Archivo+Black&family=Open+Sans:wght@600&family=Roboto+Condensed:wght@700&family=Roboto:wght@700&display=swap">
<style>
  :root {
    --brand-blue: #5a8bca;
    --brand-grey: #6f6866;
    --sign-white: #ffffff;
    --text-white: #ffffff;
  }
  * { margin: 0; padding: 0; box-sizing: border-box; }
  html, body {
    width: 1200px;
    height: 480px;
    overflow: hidden;
    background: var(--sign-white);
  }
  .billboard {
    position: relative;
    width: 1200px;
    height: 480px;
    background: var(--sign-white);
  }
  .brand-panel {
    position: absolute;
    left: 0; top: 0;
    width: 1200px;
    height: 366px;
  }
  .brand-name {
    position: absolute;
    left: 66px;
    top: 92px;
    display: flex;
    align-items: center;
    gap: 26px;
  }
  .brand-mark {
    width: 46px;
    height: 46px;
    background: var(--brand-grey);
    flex: none;
  }
  .brand-wordmark {
    font-family: "Roboto", Arial, sans-serif;
    font-weight: 700;
    font-size: 84px;
    line-height: 0.98;
    color: var(--brand-blue);
    letter-spacing: -1px;
  }
  .services {
    position: absolute;
    left: 768px;
    top: 82px;
  }
  .services-heading {
    font-family: "Roboto Condensed", "Arial Narrow", sans-serif;
    font-weight: 700;
    font-size: 40px;
    line-height: 1;
    color: var(--brand-blue);
    letter-spacing: 0.5px;
    margin-bottom: 22px;
  }
  .service-list { list-style: none; }
  .service-item {
    display: flex;
    align-items: flex-start;
    gap: 12px;
    margin-bottom: 22px;
  }
  .service-bullet { flex: none; width: 16px; height: 28px; margin-top: 2px; }
  .service-bullet--grey { fill: var(--brand-grey); }
  .service-bullet--blue { fill: var(--brand-blue); }
  .service-label {
    font-family: "Archivo Black", "Arial Black", sans-serif;
    font-size: 23px;
    line-height: 1.02;
    letter-spacing: 2px;
    color: var(--brand-grey);
    text-transform: uppercase;
  }
  .contact-band {
    position: absolute;
    left: 0; top: 366px;
    width: 1200px;
    height: 114px;
    background: var(--brand-blue);
    display: flex;
    align-items: center;
    padding-left: 40px;
    gap: 36px;
  }
  .contact-phone {
    font-family: "Roboto Condensed", "Arial Narrow", sans-serif;
    font-weight: 700;
    font-size: 86px;
    line-height: 1;
    color: var(--text-white);
    letter-spacing: 1px;
  }
  .contact-online {
    font-family: "Open Sans", Arial, sans-serif;
    font-weight: 600;
    font-size: 27px;
    line-height: 1.35;
    color: var(--text-white);
  }
</style>
</head>
<body>
  <main class="billboard">
    <section class="brand-panel">
      <div class="brand-name">
        <span class="brand-mark" aria-hidden="true"></span>
        <h1 class="brand-wordmark">Harbour<br>Frameworks</h1>
      </div>

      <div class="services">
        <h2 class="services-heading">SPECIALISING IN</h2>
        <ul class="service-list">
          <li class="service-item">
            <svg class="service-bullet service-bullet--grey" viewBox="0 0 16 28" aria-hidden="true"><polygon points="0,8 16,0 16,20 0,28"/></svg>
            <span class="service-label">Residential<br>Renovations</span>
          </li>
          <li class="service-item">
            <svg class="service-bullet service-bullet--blue" viewBox="0 0 16 28" aria-hidden="true"><polygon points="0,8 16,0 16,20 0,28"/></svg>
            <span class="service-label">Residential<br>Alterations</span>
          </li>
          <li class="service-item">
            <svg class="service-bullet service-bullet--grey" viewBox="0 0 16 28" aria-hidden="true"><polygon points="0,8 16,0 16,20 0,28"/></svg>
            <span class="service-label">Commercial</span>
          </li>
        </ul>
      </div>
    </section>

    <footer class="contact-band">
      <p class="contact-phone">022 583 7092</p>
      <div class="contact-online">
        <p class="contact-email">info@harbourframeworks.co.nz</p>
        <p class="contact-web">www.harbourframeworks.co.nz</p>
      </div>
    </footer>
  </main>
</body>
</html>
```